Brennoria Business Card Design

Primarily a Real Estate Investment company but also invests in other business ventures.
Updates

The attachments have been uploaded to give you a better perspective on what I'm looking for. Please pay close attention to the Tidal Gala Works card as a sample.Thank you.

Target Market(s)

Upper escalante individuals that would like to purchase real estate

Industry/Entity Type

Business

Contact Information for Business Card

Brennoria Holdings LLC, Sorelle A. Vantwick, CEO/MBA, 415-286-7304, Sorelle4816@mailbrook.net

Colors
0455a3
ffffff

Requirements
Must have
• Majority of card color MUST be Black ----- Like pictures 2&3
(pic4) Raised silver foil "B" to start the Brennoria name on the card.
(pic3) Love the whole layout, round edges, placement of contact info. {It is clean and elegant}
(pic1) Matte & Gloss backing
(pic2) Blue color (maybe the remainder of company name to make the card have pop of color).
Nice to have
• Silver foil siding

```html
<!DOCTYPE html>
<html lang="en">
<head>
<meta charset="utf-8">
<title>Brennoria Holdings LLC – Business Cards</title>
<link rel="stylesheet" href="https://fonts.googleapis.com/css2?family=Playfair+Display:ital,wght@0,400;1,700&family=Open+Sans:wght@400;600&display=swap">
<style>
  :root {
    --backdrop: #dcdcdd;
    --card-white: #ffffff;
    --card-black: #1b1b1c;
    --brand-blue: #0455a3;
    --light-blue: #6fa8dc;
    --silver: #d9d9d9;
    --ink: #333a44;
    --faint: #e6e9ef;
  }
  * { box-sizing: border-box; margin: 0; padding: 0; }
  html, body { width: 1200px; height: 750px; overflow: hidden; }
  body {
    background: var(--backdrop);
    font-family: "Open Sans", Arial, sans-serif;
    position: relative;
  }
  .card {
    position: absolute;
    width: 420px;
    height: 240px;
    border-radius: 20px;
    overflow: hidden;
  }
  .card--front {
    left: 150px; top: 160px;
    background: var(--card-white);
  }
  .card--back {
    left: 630px; top: 350px;
    background: linear-gradient(135deg, #262627 0%, var(--card-black) 60%, #121213 100%);
  }

  /* front: brand block */
  .brand {
    position: absolute;
    display: flex; flex-direction: column; align-items: center;
  }
  .brand__circle {
    border-radius: 50%;
    border: 3px solid var(--brand-blue);
  }
  .brand__name {
    font-family: "Playfair Display", Georgia, serif;
    font-weight: 400;
    white-space: nowrap;
  }
  .card--front .brand { left: 28px; top: 62px; width: 140px; }
  .card--front .brand__circle { width: 62px; height: 62px; }
  .card--front .brand__name { margin-top: 10px; font-size: 13px; color: var(--brand-blue); }

  .faint-circle {
    position: absolute; right: -28px; top: -30px;
    width: 110px; height: 110px; border-radius: 50%;
    background: var(--faint);
  }

  /* front: contact block */
  .contact { position: absolute; left: 206px; top: 82px; width: 200px; }
  .contact__name {
    font-family: "Playfair Display", Georgia, serif;
    font-style: italic; font-weight: 700;
    font-size: 15px; color: var(--brand-blue);
  }
  .contact__title { font-size: 7px; color: var(--ink); margin: 1px 0 0 118px; letter-spacing: .5px; }
  .contact__rule { height: 1px; background: var(--light-blue); margin: 6px 0 8px; }
  .contact__list { list-style: none; font-size: 7.5px; color: var(--ink); }
  .contact__row { display: flex; gap: 14px; margin-bottom: 6px; }
  .contact__item { display: flex; align-items: center; gap: 4px; white-space: nowrap; }
  .contact__item svg { width: 8px; height: 8px; fill: var(--brand-blue); flex: none; }

  /* back */
  .card--back .brand { left: 0; right: 0; top: 46px; }
  .card--back .brand__circle { width: 88px; height: 88px; border-color: var(--silver); }
  .card--back .brand__name { margin-top: 16px; font-size: 22px; color: var(--silver); }
</style>
</head>
<body>
  <section class="card card--front" aria-label="Business card front">
    <div class="faint-circle"></div>
    <div class="brand">
      <div class="brand__circle"></div>
      <p class="brand__name">Brennoria Holdings</p>
    </div>
    <div class="contact">
      <p class="contact__name">Sorelle A. Vantwick</p>
      <p class="contact__title">CEO/MBA</p>
      <div class="contact__rule"></div>
      <ul class="contact__list">
        <li class="contact__row">
          <span class="contact__item">
            <svg viewBox="0 0 10 10"><rect x="2.5" y="0.5" width="5" height="9" rx="1"/></svg>415-286-7304
          </span>
          <span class="contact__item">
            <svg viewBox="0 0 10 10"><path d="M2 0.5 L4 3 L3 4.2 Q4.5 6.5 5.8 7 L7 6 L9.5 8 L8.2 9.5 Q3 9 0.5 1.8 Z"/></svg>415-286-7311
          </span>
        </li>
        <li class="contact__row">
          <span class="contact__item">
            <svg viewBox="0 0 10 10"><path d="M0.5 2 H9.5 V8 H0.5 Z M0.5 2 L5 5.5 L9.5 2" /></svg>Sorelle4816@mailbrook.net
          </span>
        </li>
        <li class="contact__row">
          <span class="contact__item">
            <svg viewBox="0 0 10 10"><circle cx="5" cy="5" r="4.5"/></svg>www.brennoria-holdings.net
          </span>
        </li>
      </ul>
    </div>
  </section>

  <section class="card card--back" aria-label="Business card back">
    <div class="brand">
      <div class="brand__circle"></div>
      <p class="brand__name">Brennoria Holdings LLC</p>
    </div>
  </section>
</body>
</html>
```